Riverpeak Analytics needs new design business card

We are video surveillance and analytics software development company.
I am looking for a professional business card.
Our website is www.riverpeakanalytics.example.au
Please have a loo and get the feel for who we are and what we do.
I do not know what else to give you apart from good luck and I hope your design gets selected.
Thank you very much for participating
Business
Contact Information for Business Card
Address
27/15 Marlowe Street Fernbrook NSW 2199
Telephone 1300 582 417
Mobile 0450 731 258
email: marcus@riverpeakanalytics.example.au
name
Marcus Helvard
Position
Managing Director
Font styles to use
Other font styles liked:
- Arial
Look and feel

```html
<!DOCTYPE html>
<html lang="en">
<head>
<meta charset="utf-8">
<title>Riverpeak Analytics — Business Card</title>
<link rel="stylesheet" href="https://fonts.googleapis.com/css2?family=Source+Sans+3:wght@400;600;700&display=swap">
<style>
  :root {
    --navy: #173d69;
    --slate: #647f8f;
    --slate-dark: #46606f;
    --paper: #ffffff;
    --backdrop: #e9e7e3;
    --pattern-light: #f3f5f7;
    --pattern-mid: #e6eaee;
    --ink: #2a2a2a;
    --edge: #8a8a8a;
    --on-navy: #ffffff;
  }
  * { box-sizing: border-box; margin: 0; padding: 0; }
  html, body {
    width: 1200px;
    height: 1166px;
    overflow: hidden;
    background: var(--backdrop);
    font-family: "Source Sans 3", Arial, sans-serif;
  }
  .card {
    position: absolute;
    background: var(--paper);
    border: 1px solid var(--edge);
    overflow: hidden;
  }

  /* Front */
  .card-front { left: 57px; top: 66px; width: 894px; height: 511px; }
  .front-brand {
    position: absolute; left: 0; top: 0; width: 482px; height: 100%;
    display: flex; align-items: center; justify-content: center; gap: 18px;
  }
  .brand-square { width: 62px; height: 62px; background: var(--navy); }
  .brand-name {
    color: var(--navy); font-weight: 600; font-size: 44px; line-height: 0.95;
    text-transform: uppercase; letter-spacing: 0.5px;
  }
  .front-panel {
    position: absolute; left: 482px; top: 0; right: 0; height: 100%;
    background: var(--navy); color: var(--on-navy);
  }
  .name-band {
    position: absolute; left: -12px; right: 0; top: 84px; height: 78px;
    background: var(--slate); padding: 6px 0 0 39px;
  }
  .name-band::before {
    content: ""; position: absolute; left: 0; top: 0;
    border-right: 12px solid var(--slate-dark); border-top: 12px solid transparent;
  }
  .person-name { font-size: 31px; font-weight: 700; line-height: 1.1; }
  .person-role { font-size: 22px; font-weight: 400; line-height: 1.2; }
  .contact-list { position: absolute; left: 28px; right: 16px; top: 200px; list-style: none; }
  .contact-list li {
    display: flex; align-items: center; gap: 10px;
    font-size: 19px; height: 35.5px; white-space: nowrap;
  }
  .contact-list svg { width: 16px; height: 16px; flex: none; }
  .address { position: absolute; left: 28px; top: 366px; font-size: 19px; line-height: 30px; }

  /* Back */
  .card-back { left: 267px; top: 617px; width: 889px; height: 510px; }
  .back-pattern {
    position: absolute; inset: 0;
    background: linear-gradient(135deg, var(--pattern-light), var(--pattern-mid));
  }
  .back-brand {
    position: absolute; left: 0; right: 0; top: 118px; text-align: center;
    color: var(--navy); font-weight: 600; font-size: 100px; line-height: 96px;
    text-transform: uppercase;
  }
  .back-website {
    position: absolute; left: 0; right: 0; top: 368px; text-align: center;
    color: var(--ink); font-size: 27px; letter-spacing: 2.2px;
  }
</style>
</head>
<body>
  <section class="card card-front" aria-label="Business card front">
    <div class="front-brand">
      <span class="brand-square" aria-hidden="true"></span>
      <span class="brand-name">Riverpeak<br>Analytics</span>
    </div>
    <div class="front-panel">
      <div class="name-band">
        <p class="person-name">Marcus Helvard</p>
        <p class="person-role">Managing Director</p>
      </div>
      <ul class="contact-list">
        <li>
          <svg viewBox="0 0 24 24" aria-hidden="true"><path fill="#fff" d="M6.6 10.8a15 15 0 0 0 6.6 6.6l2.2-2.2a1 1 0 0 1 1-.25 11.4 11.4 0 0 0 3.6.57 1 1 0 0 1 1 1V20a1 1 0 0 1-1 1A17 17 0 0 1 3 4a1 1 0 0 1 1-1h3.5a1 1 0 0 1 1 1c0 1.25.2 2.45.57 3.57a1 1 0 0 1-.25 1z"/></svg>
          1300 582 417
        </li>
        <li>
          <svg viewBox="0 0 24 24" aria-hidden="true"><rect x="6" y="1" width="12" height="22" rx="2" fill="#fff"/><rect x="8" y="4" width="8" height="10" fill="#173d69"/></svg>
          0450 731 258
        </li>
        <li>
          <svg viewBox="0 0 24 24" aria-hidden="true"><path fill="#fff" d="M2 8l10-6 10 6v13H2z"/><path fill="none" stroke="#173d69" stroke-width="2" d="M3 9l9 6 9-6"/></svg>
          marcus@riverpeakanalytics.example.au
        </li>
        <li>
          <svg viewBox="0 0 24 24" aria-hidden="true"><g fill="none" stroke="#fff" stroke-width="2"><circle cx="12" cy="12" r="10"/><ellipse cx="12" cy="12" rx="4.5" ry="10"/><path d="M2 12h20M4 6.5h16M4 17.5h16"/></g></svg>
          www.riverpeakanalytics.example.au
        </li>
      </ul>
      <p class="address">27/15 Marlowe Street<br>Fernbrook NSW 2199</p>
    </div>
  </section>

  <section class="card card-back" aria-label="Business card back">
    <div class="back-pattern" role="img" aria-label="Faint repeated brand symbol pattern in pale grey"></div>
    <p class="back-brand">Riverpeak<br>Analytics</p>
    <p class="back-website">www.riverpeakanalytics.example.au</p>
  </section>
</body>
</html>
```